Clinicians Prime Bold "NOT YOUR DADDY's CARD" clear Card make the card you always wanted

I need a stand out business card, I would like it to be crazy modern using a
clear plastic 30 mil card, let this be your PHD thesis in Card Design, make it fun and cutting edge. Make it Toxicology Lab meets Night Club. Colors are tans and browns with a hint of gold, because we test PEE (urine) and we call it Liquid Gold!!

Target Market(s)

it goes to Dr. Offices, but I want them to say wow Nice card, and I want our Salesmen to say" We are not your Fathers Lab" we are NEW BOLD and Different....

Industry/Entity Type

Plastic

Contact Information for Business Card

Clinician's Prime Toxicology 2873 Fernhollow Avenue SE | Atlanta, GA 30472
Phone: 404.555.0173 | Fax: 404.555.0174 my cell phone 404.555.0198 my email is Lionel@cliniciansprimetoxicology.example

CLIA#47K9315062 | Lionel Ashcombe, CEO, GED
www.cliniciansprimetoxicology.example

Requirements
Must have
• Clear Card design, I want it to be double sided, unless you can show me a design that can only need one side because it is that GOOD
Should not have
• Should not look like a conservative lab

```html
<!DOCTYPE html>
<html lang="en">
<head>
<meta charset="utf-8">
<title>Clinician's Prime Toxicology – Clear Business Card</title>
<link rel="stylesheet" href="https://fonts.googleapis.com/css2?family=Tinos:wght@400;700&display=swap">
<style>
  :root {
    --backdrop: #c9c48f;
    --backdrop-deep: #a9a56c;
    --card-tint: rgba(250, 248, 234, 0.62);
    --card-gloss: rgba(255, 255, 255, 0.35);
    --card-edge: rgba(255, 255, 255, 0.7);
    --ink: #3f3226;
    --brand: #6e5a4b;
    --brand-sub: #9a9184;
    --accent: #7d5f45;
    --gold: #c3a24f;
    --bronze: #4e3727;
  }
  html, body {
    margin: 0;
    width: 1200px;
    height: 943px;
    overflow: hidden;
    background: var(--backdrop);
  }
  .canvas {
    position: relative;
    width: 1200px;
    height: 943px;
    background: radial-gradient(circle at 50% 50%, var(--backdrop) 40%, var(--backdrop-deep) 100%);
  }
  .card {
    position: absolute;
    left: 100px;
    top: 187px;
    width: 1000px;
    height: 568px;
    background:
      linear-gradient(125deg, var(--card-gloss) 0%, rgba(255,255,255,0) 45%, rgba(255,255,255,0.12) 100%),
      var(--card-tint);
    border: 2px solid var(--card-edge);
    border-radius: 4px;
    box-shadow: 0 0 0 1px rgba(195, 162, 79, 0.35), 0 14px 34px rgba(60, 45, 30, 0.22);
    overflow: hidden;
    font-family: "Tinos", "Times New Roman", serif;
    color: var(--ink);
  }
  .card-swoosh {
    position: absolute;
    inset: 0;
    width: 100%;
    height: 100%;
  }
  .tagline {
    position: absolute;
    left: 200px;
    top: 16px;
    margin: 0;
    font-size: 26px;
    line-height: 34px;
  }
  .brand {
    position: absolute;
    left: 68px;
    top: 96px;
  }
  .brand-dot {
    position: absolute;
    left: 0;
    top: 10px;
    width: 76px;
    height: 76px;
    border-radius: 50%;
    background: var(--accent);
  }
  .brand-name {
    position: absolute;
    left: 128px;
    top: 0;
    margin: 0;
    font-weight: 400;
    white-space: nowrap;
  }
  .brand-name .line-main {
    display: block;
    font-size: 54px;
    line-height: 70px;
    color: var(--brand);
    padding-bottom: 8px;
    border-bottom: 1px solid rgba(110, 90, 75, 0.35);
  }
  .brand-name .line-sub {
    display: block;
    font-size: 32px;
    line-height: 44px;
    padding-left: 96px;
    color: var(--brand-sub);
  }
  .contacts {
    position: absolute;
    left: 78px;
    top: 282px;
    margin: 0;
    padding: 0;
    list-style: none;
    font-size: 29px;
    line-height: 49px;
  }
  .contacts li { display: flex; align-items: center; gap: 14px; white-space: nowrap; }
  .contacts .second { margin-left: 14px; }
  .icon { width: 26px; height: 26px; fill: var(--ink); flex: none; }
  .address {
    position: absolute;
    left: 78px;
    top: 508px;
    margin: 0;
    font-size: 29px;
    line-height: 34px;
    white-space: nowrap;
  }
  .person {
    position: absolute;
    right: 42px;
    top: 292px;
    text-align: right;
  }
  .person-name {
    margin: 0;
    font-size: 32px;
    line-height: 38px;
    font-weight: 700;
    color: var(--accent);
  }
  .person-title {
    margin: 2px 0 0;
    font-size: 25px;
    line-height: 30px;
  }
  .person-clia {
    margin: 6px 0 0;
    font-size: 20px;
    line-height: 26px;
    letter-spacing: 1px;
    color: var(--accent);
  }
</style>
</head>
<body>
<main class="canvas">
  <section class="card" aria-label="Clinician's Prime Toxicology clear business card">
    <svg class="card-swoosh" viewBox="0 0 1000 568" preserveAspectRatio="none" aria-hidden="true">
      <defs>
        <linearGradient id="swoosh-top" x1="0" y1="0" x2="1" y2="1">
          <stop offset="0" stop-color="var(--bronze)"/>
          <stop offset="0.55" stop-color="var(--gold)"/>
          <stop offset="1" stop-color="var(--gold)" stop-opacity="0.2"/>
        </linearGradient>
        <linearGradient id="swoosh-bottom" x1="1" y1="1" x2="0" y2="0">
          <stop offset="0" stop-color="var(--bronze)"/>
          <stop offset="0.55" stop-color="var(--gold)"/>
          <stop offset="1" stop-color="var(--gold)" stop-opacity="0.2"/>
        </linearGradient>
      </defs>
      <path d="M0 0 H145 C75 10 25 50 0 112 Z" fill="url(#swoosh-top)"/>
      <path d="M1000 568 H852 C930 545 985 480 1000 402 Z" fill="url(#swoosh-bottom)"/>
    </svg>

    <p class="tagline">When You Need More Than Just Lab Results</p>

    <div class="brand">
      <span class="brand-dot"></span>
      <h1 class="brand-name">
        <span class="line-main">Clinician's Prime</span>
        <span class="line-sub">Toxicology</span>
      </h1>
    </div>

    <ul class="contacts">
      <li>
        <svg class="icon" viewBox="0 0 24 24" aria-label="Phone"><path d="M6.6 10.8a15 15 0 0 0 6.6 6.6l2.2-2.2c.3-.3.7-.4 1-.2 1.1.4 2.3.6 3.6.6.6 0 1 .4 1 1V20c0 .6-.4 1-1 1A17 17 0 0 1 3 4c0-.6.4-1 1-1h3.5c.6 0 1 .4 1 1 0 1.3.2 2.5.6 3.6.1.3 0 .7-.2 1z"/></svg>
        <span>404.555.0173</span>
      </li>
      <li>
        <svg class="icon" viewBox="0 0 24 24" aria-label="Mobile"><path d="M7 2h10a1 1 0 0 1 1 1v18a1 1 0 0 1-1 1H7a1 1 0 0 1-1-1V3a1 1 0 0 1 1-1zm1 3v12h8V5zm4 13.5a1 1 0 1 0 0 2 1 1 0 0 0 0-2z"/></svg>
        <span>404.555.0198</span>
        <svg class="icon second" viewBox="0 0 24 24" aria-label="Fax"><path d="M6 3h9l3 3v4H6zM3 11h18a1 1 0 0 1 1 1v7a1 1 0 0 1-1 1H3a1 1 0 0 1-1-1v-7a1 1 0 0 1 1-1zm3 3v2h4v-2z"/></svg>
        <span>404.555.0174</span>
      </li>
      <li>
        <svg class="icon" viewBox="0 0 24 24" aria-label="Email"><path d="M3 5h18a1 1 0 0 1 1 1v12a1 1 0 0 1-1 1H3a1 1 0 0 1-1-1V6a1 1 0 0 1 1-1zm1 2v.4l8 5 8-5V7z"/></svg>
        <span>lionel@cliniciansprimetoxicology.example</span>
      </li>
      <li>
        <svg class="icon" viewBox="0 0 24 24" aria-label="Website"><path d="M12 2a10 10 0 1 0 0 20 10 10 0 0 0 0-20zm0 2c.9 0 2.1 1.8 2.6 5H9.4C9.9 5.8 11.1 4 12 4zM4.3 11h3.1a18 18 0 0 0 0 2H4.3a8 8 0 0 1 0-2zm5.1 0h5.2a16 16 0 0 1 0 2H9.4a16 16 0 0 1 0-2zm7.2 0h3.1a8 8 0 0 1 0 2h-3.1a18 18 0 0 0 0-2zM9.4 15h5.2c-.5 3.2-1.7 5-2.6 5s-2.1-1.8-2.6-5z"/></svg>
        <span>www.cliniciansprimetoxicology.example</span>
      </li>
    </ul>

    <p class="address">2873 Fernhollow Avenue SE &nbsp;|&nbsp; Atlanta, GA 30472</p>

    <div class="person">
      <p class="person-name">Lionel Ashcombe</p>
      <p class="person-title">CEO, GED</p>
      <p class="person-clia">CLIA#47K9315062</p>
    </div>
  </section>
</main>
</body>
</html>
```